Window Graphics ‘Opening Soon’ for new Jewellery Boutique

We want to fully cover the shop window for a duration of 6 weeks whilst the refurbishment is going on. The window graphics should be cool, sexy and sophisticated. The graphics should include our company logo ‘THE COPPER LANTERN’ in Gills Sans Font. The shop will be an upmarket jewellery watch shop.

Target Market(s)

Jewellery customers

Industry/Entity Type

Jewellery

Colors

Designer to choose colors to be used in the design.

Requirements
Must have
• Must be loud graphics that catch your attention when walking past. I have provided a graphics example where the colour palette is black, white and shocking pink!
Nice to have
• The Boss is Back…. The Copper Lantern Proudly present a new masterpiece coming soon….

```html
<!DOCTYPE html>
<html lang="en">
<head>
<meta charset="utf-8">
<title>The Copper Lantern – Window Graphics</title>
<link href="https://fonts.googleapis.com/css2?family=Barlow+Condensed:wght@600;700;800&family=Cabin:wght@400;500&display=swap" rel="stylesheet">
<style>
  :root {
    --backdrop: #2468b0;
    --panel-light: #f7f7f8;
    --panel-mid: #dcdde0;
    --ink: #151515;
    --pink: #e2087f;
    --gold: #c9a24a;
    --charcoal: #2c2c2e;
  }
  * { box-sizing: border-box; margin: 0; padding: 0; }
  html, body { width: 1015px; height: 1200px; overflow: hidden; }
  body { background: var(--backdrop); position: relative; }

  .panel {
    position: absolute;
    top: 426px;
    height: 348px;
    overflow: hidden;
    background: linear-gradient(135deg, var(--panel-light) 0%, var(--panel-mid) 45%, var(--panel-light) 70%, var(--panel-mid) 100%);
  }
  .panel--left { left: 64px; width: 148px; }
  .panel--main { left: 248px; width: 535px; }
  .panel--right { left: 813px; width: 140px; }

  .brand-name {
    position: absolute; left: 0; right: 0; top: 64px;
    text-align: center;
    font-family: "Gill Sans", "Cabin", sans-serif;
    font-weight: 400;
    font-size: 9.5px;
    line-height: 1;
    color: var(--ink);
    white-space: nowrap;
  }

  .display {
    font-family: "Barlow Condensed", sans-serif;
    font-weight: 800;
    color: var(--ink);
    line-height: 1;
    white-space: nowrap;
  }

  .boss-line { position: absolute; left: 0; right: 0; text-align: center; }
  .boss-line--the { top: 134px; font-size: 41px; }
  .boss-line--boss { top: 178px; font-size: 57px; }
  .boss-line--back { top: 237px; font-size: 35px; }

  .product { position: absolute; }
  .product--necklace { left: 35px; top: 66px; width: 106px; height: 137px;
    background: radial-gradient(ellipse at 50% 35%, #4a4a4d 0%, var(--charcoal) 60%, #1a1a1b 100%);
    border-radius: 40% 40% 8px 8px; }
  .product--watch { left: 36px; top: 249px; width: 103px; height: 66px; border-radius: 6px;
    background: linear-gradient(90deg, #a9822f 0%, var(--gold) 45%, #efe7d0 75%, #b8913d 100%); }
  .product--bangles { left: 411px; top: 213px; width: 96px; height: 58px; border-radius: 29px;
    background: linear-gradient(90deg, #c99f5f 0%, #e8c98e 50%, #c39660 100%); }

  .announce-intro { position: absolute; left: 171px; top: 38px; font-size: 17px; font-weight: 700; }
  .announce-title { position: absolute; left: 170px; top: 57px; font-size: 43px; }
  .announce-coming { position: absolute; left: 168px; top: 97px; font-size: 90px; line-height: 0.83; color: var(--pink); }

  .reveal {
    position: absolute; left: 175px; top: 281px; height: 34px;
    padding-left: 11px; border-left: 2px solid var(--pink);
    font-family: "Gill Sans", "Cabin", sans-serif; color: var(--pink);
    font-size: 18.5px; line-height: 1.05; white-space: nowrap;
  }
  .reveal sup { font-size: 10px; }

  .location-pin { position: absolute; left: 63px; top: 194px; }
  .location-address {
    position: absolute; left: 0; right: 0; top: 223px;
    text-align: center; font-size: 14px; font-weight: 700; line-height: 15.5px;
  }
</style>
</head>
<body>

  <section class="panel panel--left">
    <p class="brand-name">THE COPPER LANTERN</p>
    <p class="boss-line boss-line--the display">THE</p>
    <p class="boss-line boss-line--boss display">BOSS</p>
    <p class="boss-line boss-line--back display">IS BACK</p>
  </section>

  <section class="panel panel--main">
    <div class="product product--necklace" role="img" aria-label="Pearl necklace displayed on a black bust stand"></div>
    <div class="product product--watch" role="img" aria-label="Gold diamond-set wristwatch"></div>
    <div class="product product--bangles" role="img" aria-label="Pair of engraved gold bangles"></div>

    <p class="announce-intro display">THE COPPER LANTERN PROUDLY PRESENT</p>
    <p class="announce-title display">A NEW MASTERPIECE</p>
    <p class="announce-coming display">COMING<br>SOON</p>

    <div class="reveal">
      <p>EXISTING FRONT ELEVATION</p>
      <p>04<sup>th</sup> OCTOBER 2021</p>
    </div>
  </section>

  <section class="panel panel--right">
    <p class="brand-name">THE COPPER LANTERN</p>
    <svg class="location-pin" width="14" height="20" viewBox="0 0 14 20" aria-hidden="true">
      <path d="M7 0C3.1 0 0 3.1 0 7c0 5 7 13 7 13s7-8 7-13c0-3.9-3.1-7-7-7z" fill="#e2087f"/>
      <circle cx="7" cy="7" r="2.8" fill="#f7f7f8"/>
    </svg>
    <p class="location-address display">VELLORA LONDON<br>14 ASHBURY LANE<br>MERRIDEN GARDENS<br>EC9X 4QT</p>
  </section>

</body>
</html>
```